Exciting Racehorse Sale Information Brochure Project

We are a company based in Australia that sells shares in race horses. We syndicate the hroses into smaller shares which we sell, after wich we manage the horses throughout their racing career, gaining the maximum potential from the horse and providing the most enjoyable experience for the owners/investors. We require our information brochure to be updated. The brochure is customised for each horse we are selling so it must be in a format that we can edit ourselves once created. It would be handy to have a 'shell' in which we can then edit the content.

I have attached a copy of the current brochure requiring an update. The look and feel that we are after is very professional, yet exciting and fun.

Our main company colours are red and white so we would like to see these imcorporated into the design.

The design should communicate experience, success, excitement and professionalism.

The font within our logo is "fertigo regular" if you wish to use it in the document.
Updates

Logo file now working - file #23

Target Market(s)

Adults, both genders, all education levels and occupations buy racehorse shares so it needs to be for a broad audience

Industry/Entity Type

Racing

Requirements
Must have
• Must include our logo and some of the images of our horses/clients that have been provided.

Must also have scope to include all the information in the example we have provioded.

The design must be in a format that we can customise all content for each individual brochure sent.

Must be under 5MG so it can be sent via email
Nice to have
• * Some type of heading for each section eg. 'Prizemoney', 'Management', 'The Trainer' etc.
* A coverpage where we can incorporate a photo and the name of the specific horse we are selling.
* We are open to your thoughts and creative designs however one possibility for the coverpage may include a montage of photos and logo at the top with a photo of the specific horse and its name below??

```html
<!DOCTYPE html>
<html lang="en">
<head>
<meta charset="utf-8">
<title>The Horse – Syndicate Brochure</title>
<link href="https://fonts.googleapis.com/css2?family=Arimo:wght@400;700&display=swap" rel="stylesheet">
<style>
  :root {
    --brand-red: #ff0000;
    --ink: #1a1a1a;
    --paper: #ffffff;
    --photo-dark: #2a1a12;
    --photo-mid: #5b3a26;
    --photo-light: #8fa08a;
  }
  html, body {
    margin: 0;
    padding: 0;
    overflow: hidden;
    background: var(--paper);
  }
  .page {
    position: relative;
    width: 1200px;
    height: 931px;
    overflow: hidden;
    background: var(--paper);
    font-family: "Arimo", Arial, sans-serif;
    color: var(--ink);
  }
  .top-band {
    position: absolute;
    left: 0; top: 0;
    width: 1200px; height: 46px;
    background: var(--brand-red);
  }
  .horse-photo {
    position: absolute;
    left: 860px; top: 46px;
    width: 340px; height: 524px;
    background:
      radial-gradient(ellipse at 60% 55%, var(--photo-mid) 0%, var(--photo-dark) 45%, transparent 70%),
      linear-gradient(160deg, var(--photo-light) 0%, #6f7f6a 40%, #3a3028 100%);
  }
  .section-title {
    position: absolute;
    left: 49px; top: 88px;
    margin: 0;
    font-size: 24px;
    font-weight: 700;
    letter-spacing: 0.2px;
  }
  .copy {
    position: absolute;
    left: 49px;
    width: 780px;
    margin: 0;
    font-size: 17.4px;
    line-height: 28.4px;
  }
  .copy.highlight {
    font-size: 24px;
    font-weight: 700;
    line-height: 33.6px;
  }
  .p1 { top: 145px; }
  .p2 { top: 250px; }
  .p3 { top: 371px; }
  .p4 { top: 479px; }
  .p5 { top: 649px; }
  .p6 { top: 759px; }
  .cta-box {
    position: absolute;
    left: 927px; top: 672px;
    width: 273px; height: 259px;
    background: var(--brand-red);
  }
  .cta-text {
    position: absolute;
    left: 27px; top: 42px;
    margin: 0;
    color: var(--paper);
    font-size: 24.5px;
    font-weight: 700;
    line-height: 32px;
  }
</style>
</head>
<body>
<div class="page">
  <div class="top-band"></div>

  <div class="horse-photo" role="img" aria-label="Photograph of a bay racehorse's head wearing a bridle, at the racecourse"></div>

  <h2 class="section-title">THE HORSE</h2>

  <p class="copy p1">By a Champion 2yo, out of a 2yo stakes winner producing family and trained by the best 2yo trainer. It’s no surprise we believe this exciting colt is ideally suited to next year’s Summer Millions and then Silver Boot. The targets have been set.</p>

  <p class="copy highlight p2">There has been a total of 15 runners bred on the same breeding cross as this colt head to the races for an incredible 14 winners (93%) including 3 stakeswinners (20%).</p>

  <p class="copy p3">When you drill down even further, there have been 8 colts from this cross hit the track and all 8 have been winners (100%) of which 2 have been stakeswinners (25%). These stats are simply exceptional! In fact, we have never seen stats like these so high before.</p>

  <p class="copy p4">This outstanding colt is not only bred to be a 2yo runner but he looks a real 2yo runner too. In fact, he looks the spitting image of his dad (who was a Champion 2yo runner). You could just about throw a saddle on him and send him around now. He looks physically ready and he is a very athletic style of colt who moves majestically across the ground. The natural runners just stand out and this bloke is one of them.</p>

  <p class="copy p5">This colt like his dad (SILVERBRUMBY), is a strong, athletic and robust type. Very much in the mould of his great-grand father, the almighty STORMHAVEN. The STORMHAVEN influence in this colt’s make-up is an obvious one.</p>

  <p class="copy p6">“He is a very athletic style of colt who strikes me as a real running 2YO type. In fact, he is the ideal type of horse to have a crack with at the Summer Millions 2YO race. He is strong and well mannered for a colt and has a particularly fluent action and nice stride on him. I look forward to getting him to the races.” Martin Hale (Sydney’s leading 2yo trainer.)</p>

  <div class="cta-box">
    <p class="cta-text">Race a<br>SILVERBRUMBY<br>colt with<br>Crimson Crest &amp;<br>Martin Hale</p>
  </div>
</div>
</body>
</html>
```